Strategy and Technology Consulting - Our Story and Values Page

Interior Page design – Our History and Our Values

Our homepage has been designed and we are looking for a design for one of the interior pages. This interior page tells the story of Our History and Our Values

Because the homepage has been designed, we would like this interior page to reflect the design of the homepage without being a mirror image of the homepage.

This site will be implemented in WordPress using the Elementor framework.

Font: Poppins medium and Poppins dark
Illustrations: Our homepage illustrations were designed by “Welmo 1974” on Pixaborne. Compatible original or stock illustrations are welcome. Stock photography is also welcome. Welmo is also available through Welmo Trastek on Folivane

Uploaded Files
• Homepage design – this is the design we will use for our homepage. Contest entries should reflect this basic style but should be distinctly different from the homepage.
• Our History and Our Values – Wireframe – the basic layout of the page we are looking for.
• Our History and Our Values – Word document with the text supporting the wireframe.
• Color Palette – please use colors compatible with the palette attached.

Our Story - timeline
There is a timeline element in the wireframe. The wireframe displays this as a series of chevrons (arrows), but it does not need to be. Creativity in display of the timeline is appreciated.

Our Values
If you look at the Word document, you will see that there are a lot of words on the page. The winning design will present the information in a way that engages the user without overwhelming them with too much to read. For example, they may click on a value and see more information.

Target Market(s)

CIO's and Technology Executives

Number of Pages Required

1 page

Font styles to use
Sans Serif
Other font styles liked:
• Poppin

Requirements
Must have
• A timeline element, all of our values
Nice to have
• Clever timeline display

```html
<!DOCTYPE html>
<html lang="en">
<head>
<meta charset="utf-8">
<title>Climbrex – Our Story &amp; Our Values</title>
<link href="https://fonts.googleapis.com/css2?family=Poppins:wght@300;400;500;600;700;800&display=swap" rel="stylesheet">
<style>
:root{
  --blue-deep:#22568e;
  --blue-mid:#3f76a8;
  --blue-light:#bcd6ea;
  --blue-pale:#dbe7f2;
  --yellow:#f0b323;
  --yellow-soft:#f6cc5c;
  --slate:#44536d;
  --slate-dark:#3a4860;
  --heading:#3d4a63;
  --text:#5f6b7d;
  --line:#d5dbe3;
  --white:#ffffff;
}
*{margin:0;padding:0;box-sizing:border-box}
html,body{width:1200px;height:3492px;overflow:hidden}
body{position:relative;font-family:"Poppins",sans-serif;background:var(--white);color:var(--text)}
.abs{position:absolute}

/* header */
.site-header{position:absolute;left:0;top:0;width:1200px;height:94px;background:var(--white)}
.brand{position:absolute;display:flex;align-items:center;gap:8px;font-family:"Poppins",sans-serif;font-weight:400;color:#8f97a3}
.brand-dot{width:10px;height:10px;background:var(--blue-mid);border-radius:50%}
.site-header .brand{left:92px;top:22px;font-size:44px;line-height:50px}
.main-nav{position:absolute;left:544px;top:36px;display:flex;gap:24px;align-items:center;font-size:13px;font-weight:500;color:var(--heading);text-transform:uppercase}
.main-nav .chev{display:inline-block;width:6px;height:6px;border-right:1.5px solid var(--heading);border-bottom:1.5px solid var(--heading);transform:rotate(45deg);margin-left:6px;position:relative;top:-3px}
.btn-yellow{position:absolute;background:var(--yellow);color:var(--white);font-weight:700;text-transform:uppercase;border-radius:20px;display:flex;align-items:center;justify-content:center}
.site-header .btn-yellow{left:980px;top:27px;width:132px;height:38px;font-size:12px}

/* story */
.story-bg{position:absolute;left:0;top:94px}
.story-title{position:absolute;left:0;width:1200px;top:180px;text-align:center;color:var(--white);font-size:52px;font-weight:800}
.year{position:absolute;color:var(--white);font-weight:700;font-size:18px;line-height:22px;text-align:center}
.story-col{position:absolute;top:404px;height:152px;border-left:4px solid var(--blue-light);padding-left:22px;color:var(--white);font-size:13px;line-height:16px;font-weight:500}
.story-col.mid{border-left-color:var(--yellow)}
.story-col li{list-style:none;position:relative;padding-left:14px;margin-bottom:11px}
.story-col li::before{content:"";position:absolute;left:0;top:6px;width:5px;height:5px;border-radius:50%;background:var(--blue-light)}
.story-col li.sub{padding-left:30px;margin-bottom:6px}
.story-col li.sub::before{left:14px;top:8px;width:6px;height:1.5px;border-radius:0;background:var(--white)}

/* values */
.values-title{position:absolute;left:0;width:1200px;top:768px;text-align:center;color:var(--heading);font-size:50px;font-weight:800}
.values-axis{position:absolute;left:599px;top:861px;height:1817px;border-left:1.5px dashed var(--line)}
.axis-dot{position:absolute;left:595px;width:10px;height:10px;border-radius:50%;background:#7e8797;box-shadow:0 0 0 4px #eef1f5}
.value{position:absolute;width:469px}
.value.right{left:641px}
.value.left{left:91px;text-align:right}
.value h3{color:var(--heading);font-size:21px;font-weight:700;line-height:28px;margin-bottom:8px}
.value p{font-size:14px;line-height:19.7px;font-weight:400}
.illustration{position:absolute;border-radius:18px;background:linear-gradient(135deg,#fbe2a0 0%,#f3c24d 45%,#c3d3ee 100%);opacity:.85}

/* contact band */
.cta-pill{position:absolute;left:137px;top:2782px;width:923px;height:208px;border-radius:104px;background:var(--yellow)}
.cta-pill h2{position:absolute;left:81px;top:80px;color:var(--white);font-size:34px;font-weight:800;line-height:44px}
.btn-white{position:absolute;left:698px;top:76px;width:167px;height:54px;border-radius:27px;background:var(--white);color:var(--heading);font-size:14px;font-weight:500;display:flex;align-items:center;justify-content:center}

/* footer */
.footer-col{position:absolute;top:3140px;color:var(--white)}
.footer-col h4{font-size:20px;font-weight:700;line-height:32px;margin-bottom:12px}
.footer-col li{list-style:none;font-size:13px;line-height:18px;margin-bottom:13px;color:#e6eaf0;position:relative;padding-left:14px}
.footer-col li::before{content:"";position:absolute;left:0;top:6px;width:5px;height:5px;border-right:1.5px solid #e6eaf0;border-bottom:1.5px solid #e6eaf0;transform:rotate(-45deg)}
.contact-item{position:relative;padding-left:23px;font-size:13px;line-height:17px;color:#e6eaf0;margin-bottom:18px}
.contact-item svg{position:absolute;left:0;top:2px}
.site-footer .brand{left:119px;top:3168px;font-size:62px;line-height:70px;color:#c3c9d2}
.social{position:absolute;top:3244px;width:42px;height:42px;border-radius:50%;background:#6c7a91}
.site-footer .btn-yellow{left:203px;top:3314px;width:132px;height:38px;font-size:12px}
.copyright-bar{position:absolute;left:0;top:3431px;width:1200px;height:61px;background:var(--slate-dark);color:var(--white);font-size:13px;font-weight:500;display:flex;align-items:center;justify-content:center}
.chat-btn{position:absolute;left:1134px;top:3408px;width:50px;height:50px;border-radius:50%;background:var(--yellow);display:flex;align-items:center;justify-content:center}
</style>
</head>
<body>

<header class="site-header">
  <div class="brand"><span class="brand-dot"></span>Climbrex</div>
  <nav class="main-nav">
    <svg width="16" height="14" viewBox="0 0 16 14"><path d="M8 1 1 7h2v6h4V9h2v4h4V7h2z" fill="#8f97a3"/></svg>
    <span>About us<i class="chev"></i></span>
    <span>Services<i class="chev"></i></span>
    <span>Insights<i class="chev"></i></span>
    <span>Join us<i class="chev"></i></span>
  </nav>
  <div class="btn-yellow">Contact us</div>
</header>

<!-- Our Story -->
<svg class="story-bg" width="1200" height="630" viewBox="0 94 1200 630" aria-hidden="true">
  <defs>
    <linearGradient id="storyGrad" x1="0" y1="0" x2="1" y2="0.6">
      <stop offset="0" stop-color="#6b9bc3"/>
      <stop offset="0.45" stop-color="#2e6399"/>
      <stop offset="1" stop-color="#22568e"/>
    </linearGradient>
  </defs>
  <path d="M0 94H1200V560C1120 600 1020 715 860 700C720 690 620 705 520 705C400 705 280 600 150 610C80 615 30 630 0 640Z" fill="#d8e2ec" transform="translate(14,10)"/>
  <path d="M0 94H1200V550C1110 590 1010 705 850 692C710 682 610 700 490 700C370 700 260 595 140 605C70 610 25 625 0 635Z" fill="url(#storyGrad)"/>
  <!-- timeline band -->
  <rect x="209" y="302" width="230" height="82" fill="#bcd6ea"/>
  <rect x="439" y="302" width="205" height="82" fill="#f0b323"/>
  <rect x="644" y="302" width="250" height="82" fill="#bcd6ea"/>
  <polygon points="398,294 440,266 510,343 440,400 398,392 455,343" fill="#9ec3e2"/>
  <polygon points="420,300 440,282 500,343 440,394 420,386 470,343" fill="#cfe2f1"/>
  <polygon points="634,294 680,266 748,343 680,400 634,392 695,343" fill="#e7a91b"/>
  <polygon points="656,300 680,282 738,343 680,394 656,386 706,343" fill="#f6d06a"/>
  <polygon points="870,294 914,266 983,343 914,400 870,392 930,343" fill="#9ec3e2"/>
  <polygon points="892,300 914,282 972,343 914,394 892,386 942,343" fill="#cfe2f1"/>
</svg>

<h1 class="story-title">Our Story</h1>
<div class="year" style="left:259px;top:322px;width:80px">2017<br>2019</div>
<div class="year" style="left:515px;top:322px;width:80px">2020<br>2021</div>
<div class="year" style="left:738px;top:322px;width:100px">2022 &amp;<br>Onward</div>

<ul class="story-col" style="left:237px;width:215px">
  <li>Growth Strategy Focus</li>
  <li>Consistent, Modest Growth</li>
  <li>Preliminary Focus on Technology</li>
  <li><b>Eureka!</b> Implementing strategy is hard.</li>
</ul>
<ul class="story-col mid" style="left:473px;width:215px">
  <li>Pandemic Pauses Growth</li>
  <li>Rethinking :</li>
  <li class="sub">the business model</li>
  <li class="sub">the delivery model</li>
</ul>
<ul class="story-col" style="left:709px;width:215px">
  <li>Leadership Team for Focus on Essential Areas</li>
  <li>Rapid Growth</li>
  <li>Customer Success</li>
</ul>

<!-- Our Values -->
<h2 class="values-title">Our Values</h2>
<div class="values-axis"></div>

<div class="illustration" role="img" aria-label="Illustration of a confident man with arms crossed in front of rising arrows" style="left:222px;top:854px;width:323px;height:244px"></div>
<div class="axis-dot" style="top:971px"></div>
<div class="value right" style="top:920px">
  <h3>The Value of Every Human.&nbsp; Regardless.</h3>
  <p>Each person's unique experiences and perspectives add vibrant hues to the tapestry of our shared existence.&nbsp; In a world where diversity paints the canvas of humanity, true beauty is found in recognizing the inherent and incalculable value of every human being.</p>
</div>

<div class="illustration" role="img" aria-label="Illustration of a woman fitting puzzle pieces together beside a check mark" style="left:640px;top:1098px;width:316px;height:244px"></div>
<div class="axis-dot" style="top:1238px"></div>
<div class="value left" style="top:1176px">
  <h3>Collaboration</h3>
  <p>Collaboration in work transforms individual endeavors into symphonies of collective achievement. Through collaboration, diverse talents converge, fostering a rich exchange of ideas that amplifies creativity, accelerates progress, and brings forth solutions beyond what a single mind could conceive.</p>
</div>

<div class="illustration" role="img" aria-label="Illustration of a man pointing at a chart on a monitor" style="left:222px;top:1383px;width:323px;height:247px"></div>
<div class="axis-dot" style="top:1500px"></div>
<div class="value right" style="top:1449px">
  <h3>Passion</h3>
  <p>Passion infuses our work with energy, transforming routine tasks into opportunities for creativity and innovation. Fueled by passion, individuals become unstoppable forces, driven to overcome challenges and achieve remarkable outcomes that benefit them and inspire those around them.</p>
</div>

<div class="illustration" role="img" aria-label="Illustration of a woman working at a large computer screen" style="left:640px;top:1634px;width:316px;height:244px"></div>
<div class="axis-dot" style="top:1773px"></div>
<div class="value left" style="top:1720px">
  <h3>Excellence</h3>
  <p>Excellence isn't a destination; it's a continuous journey of refinement and growth. Striving for excellence cultivates a culture of continuous improvement, fostering innovation, credibility, and a lasting impact that resonates far beyond the immediate task.</p>
</div>

<div class="illustration" role="img" aria-label="Illustration of a man presenting video content on screens" style="left:210px;top:1912px;width:335px;height:244px"></div>
<div class="axis-dot" style="top:2025px"></div>
<div class="value right" style="top:1971px">
  <h3>Tenacity</h3>
  <p>Tenacity is the unwavering anchor that keeps us grounded amidst adversity, propelling us forward when faced with obstacles. The resilience to persist, adapt, and learn from setbacks leads to the mastery of skills and the fulfillment of ambitious goals.</p>
</div>

<div class="illustration" role="img" aria-label="Illustration of a woman at a laptop with a lightbulb idea" style="left:640px;top:2156px;width:321px;height:237px"></div>
<div class="axis-dot" style="top:2291px"></div>
<div class="value left" style="top:2237px">
  <h3>Solution Mindset</h3>
  <p>A solution mindset is the compass that directs our focus from problems to possibilities. It empowers us to navigate challenges with a proactive mindset, igniting a journey of exploration and innovation that not only resolves issues but also paves the way for continuous growth and success.</p>
</div>

<div class="illustration" role="img" aria-label="Illustration of a man using a tablet next to a phone screen with messages" style="left:208px;top:2434px;width:334px;height:244px"></div>
<div class="axis-dot" style="top:2546px"></div>
<div class="value right" style="top:2492px">
  <h3>Generosity</h3>
  <p>Generosity creates a virtuous cycle of goodwill, fostering a sense of unity and shared purpose among colleagues. By freely sharing knowledge, support, and resources, we uplift those around us and contribute to a collaborative environment where collective achievements flourish.</p>
</div>

<!-- Footer -->
<footer class="site-footer">
  <svg class="abs" style="left:0;top:2790px" width="1200" height="641" viewBox="0 2790 1200 641" aria-hidden="true">
    <defs>
      <linearGradient id="footGrad" x1="0" y1="0" x2="0" y2="1">
        <stop offset="0" stop-color="#3c4a63"/>
        <stop offset="1" stop-color="#55647e"/>
      </linearGradient>
    </defs>
    <path d="M0 2808C120 2830 180 2920 300 2960C460 3010 560 2930 700 2940C860 2950 960 3020 1080 2950C1130 2920 1170 2880 1200 2870V3431H0Z" fill="url(#footGrad)"/>
    <path d="M300 3040C420 3070 520 3010 640 3020C780 3030 880 3080 1010 3050C1100 3030 1160 3030 1200 3040V3060C1150 3050 1100 3060 1010 3080C880 3110 780 3055 640 3045C520 3035 420 3090 300 3060Z" fill="#dde3ea"/>
  </svg>

  <div class="cta-pill">
    <h2>Contact us to learn more</h2>
    <div class="btn-white">CONTACT US</div>
  </div>

  <div class="brand"><span class="brand-dot"></span>Climbrex</div>
  <span class="social" style="left:176px"></span>
  <span class="social" style="left:226px"></span>
  <span class="social" style="left:277px"></span>
  <span class="social" style="left:327px"></span>
  <div class="btn-yellow">Contact us</div>

  <div class="footer-col" style="left:491px">
    <h4>Quick links</h4>
    <ul><li>Home</li><li>About Us</li><li>Services</li><li>Insights</li><li>Join Us</li><li>Contact Us</li></ul>
  </div>
  <div class="footer-col" style="left:668px">
    <h4>Our Services</h4>
    <ul><li>Business Transformation</li><li>ERP Implementations</li><li>ERP Solutions</li><li>BI and Data</li><li>Building the Right Team...</li></ul>
  </div>
  <div class="footer-col" style="left:899px">
    <h4>Contact info</h4>
    <div class="contact-item"><svg width="13" height="10" viewBox="0 0 13 10"><rect width="13" height="10" rx="1" fill="#f0b323"/><path d="M1 1l5.5 4.5L12 1" stroke="#44536d" fill="none"/></svg>Email:<br>hello@climbrex-mail.com</div>
    <div class="contact-item"><svg width="13" height="13" viewBox="0 0 13 13"><path d="M3 1l2 3-1.5 1.5c.8 1.8 2.2 3.2 4 4L9 8l3 2-1 2.5C6 12 1 7 .5 2z" fill="#f0b323"/></svg>Phone:<br>+44 100 000 0199</div>
    <div class="contact-item"><svg width="11" height="14" viewBox="0 0 11 14"><path d="M5.5 0A5.5 5.5 0 0 0 0 5.5C0 9.5 5.5 14 5.5 14S11 9.5 11 5.5A5.5 5.5 0 0 0 5.5 0z" fill="#f0b323"/><circle cx="5.5" cy="5.5" r="2" fill="#44536d"/></svg>Location:<br>Some address line goes<br>here city name</div>
  </div>

  <div class="copyright-bar">© Climbrex Design 2023, All Rights Reserved</div>
  <div class="chat-btn"><svg width="24" height="22" viewBox="0 0 24 22"><path d="M3 2h18a2 2 0 0 1 2 2v10a2 2 0 0 1-2 2H9l-5 4v-4H3a2 2 0 0 1-2-2V4a2 2 0 0 1 2-2z" fill="#fff"/><circle cx="8" cy="9" r="1.4" fill="#f0b323"/><circle cx="12" cy="9" r="1.4" fill="#f0b323"/><circle cx="16" cy="9" r="1.4" fill="#f0b323"/></svg></div>
</footer>

</body>
</html>
```